Lanterns? Lanterns? Walking Where the Quiet Morning Leads

I'm doing a series of ebooks that are 50 to 100 pages. The cover needs to be captivating because most of the traffic will be online. This book is about decision making and the steps that God offers to help us make good ones. If it works, perhaps we can silhouette or creatively show common questions: Is she the one? Is this job right for me? etc, or maybe just list some common areas: Entertainment, Music, Marriage, Sex, Modesty, etc. Just brainstorming.

```html
<!DOCTYPE html>
<html lang="en">
<head>
<meta charset="utf-8">
<title>Lanterns? Lanterns? — Ebook Cover</title>
<link rel="stylesheet" href="https://fonts.googleapis.com/css2?family=Fraunces:opsz,wght@9..144,900&family=Montserrat:wght@800&display=swap">
<style>
  :root {
    --page: #ffffff;
    --cover: #f2b467;
    --title: #b35c00;
    --subtitle: #ffffff;
    --art-sky: #a3eef8;
    --art-coral: #f77b6a;
    --art-pink: #f79ee6;
    --art-green: #5ee68a;
    --art-yellow: #f6d80e;
    --art-cream: #f6e68c;
    --art-orange: #f5920f;
    --art-blue: #62aef2;
    --art-steel: #4f86c6;
    --art-violet: #c99be8;
  }
  * { margin: 0; padding: 0; box-sizing: border-box; }
  html, body {
    width: 1200px;
    height: 900px;
    overflow: hidden;
    background: var(--page);
  }
  .canvas {
    position: relative;
    width: 1200px;
    height: 900px;
  }
  .cover {
    position: absolute;
    left: 343px;
    top: 72px;
    width: 537px;
    height: 759px;
    background: var(--cover);
    box-shadow: 0 1px 3px rgba(0,0,0,0.12);
  }
  .cover-title {
    position: absolute;
    left: 45px;
    top: 32px;
    width: 444px;
    height: 34px;
    display: block;
    overflow: visible;
  }
  .cover-title text {
    font-family: "Fraunces", "Cooper Black", Georgia, serif;
    font-weight: 900;
    font-size: 34px;
    fill: var(--title);
  }
  .cover-art {
    position: absolute;
    left: 44px;
    top: 73px;
    width: 445px;
    height: 628px;
    overflow: hidden;
    background-color: var(--cover);
    background-image:
      radial-gradient(ellipse 30% 22% at 12% 4%, var(--art-coral) 0%, transparent 100%),
      radial-gradient(ellipse 40% 30% at 22% 22%, var(--art-sky) 20%, transparent 100%),
      radial-gradient(ellipse 18% 30% at 50% 18%, var(--art-yellow) 20%, transparent 100%),
      radial-gradient(ellipse 16% 28% at 66% 22%, var(--art-violet) 10%, transparent 100%),
      radial-gradient(ellipse 34% 46% at 90% 34%, var(--art-green) 30%, transparent 100%),
      radial-gradient(ellipse 26% 24% at 38% 48%, var(--art-orange) 20%, transparent 100%),
      radial-gradient(ellipse 22% 16% at 94% 64%, var(--art-blue) 10%, transparent 100%),
      radial-gradient(ellipse 24% 18% at 18% 66%, var(--art-pink) 0%, transparent 100%),
      radial-gradient(ellipse 34% 28% at 22% 86%, var(--art-cream) 20%, transparent 100%),
      radial-gradient(ellipse 30% 30% at 76% 92%, var(--art-steel) 20%, transparent 100%),
      radial-gradient(ellipse 36% 36% at 80% 78%, var(--art-pink) 30%, transparent 100%);
  }
  .cover-subtitle {
    position: absolute;
    left: 45px;
    top: 709px;
    width: 444px;
    height: 22px;
    display: block;
    overflow: visible;
  }
  .cover-subtitle text {
    font-family: "Montserrat", "Helvetica Neue", Arial, sans-serif;
    font-weight: 800;
    font-size: 17px;
    fill: var(--subtitle);
  }
</style>
</head>
<body>
  <main class="canvas">
    <section class="cover" aria-label="Ebook cover">
      <svg class="cover-title" viewBox="0 0 444 34" aria-label="Lanterns? Lanterns?">
        <text x="0" y="30" textLength="444" lengthAdjust="spacingAndGlyphs">LANTERNS?LANTERNS?</text>
      </svg>
      <div class="cover-art" role="img" aria-label="Colourful illustration of impossible interlocking staircases, arches and walls in sky blue, coral, yellow, green, orange, pink and blue with halftone shading"></div>
      <svg class="cover-subtitle" viewBox="0 0 444 22" aria-label="Walking Where the Quiet Morning Leads">
        <text x="0" y="18" textLength="444" lengthAdjust="spacingAndGlyphs">WALKING WHERE THE QUIET MORNING LEADS</text>
      </svg>
    </section>
  </main>
</body>
</html>
```